Tiny Brookvale - Haircuts

Flyer - Tiny Brookvale is a independent kids clothes, babywear and toy shop. We sell some of the most beautiful clothes and toys available. We have recently started to do haircuts for kids and we need a flyer to promote this.
The design should be in line with the boutique nature of the shop, the care and attention we pay to each of our customers and lovely items we have for sale. This flyer is primarily to promote the availability of haircuts but will be circulated in the local area to also promote awareness of the shop which only opened a few months ago.

The flyer design should be double sided A5

One side should be all dark blue with just the logo with hair dryer and 'Tiny Brookvale' text with the text below:

Have your child's hair cut at our new salon just for little people! Call 0207 514 0627 or email shop@tinybrookvale.com to book an appointment.

Follow us on twitter @tinybrookvale

We use the blue background logo and this blue should be the predominant color of the flyer.

Target Market(s)

Discerning parents, mid to high end consumers, high earners..

Industry/Entity Type

Shop

Font styles to use
Other font styles liked:
• Sa

Colors
3177b5
3377b5
85acd3
3076b4

Requirements
Must have
• It would be great to have generic shot of a kid having their haircut. A s hot without copy right issues please.
• Shot of hairdressing, show what the shop looks like.
• Sophisticated feel.
Should not have
• Not a cartoon feel

```html
<!DOCTYPE html>
<html lang="en">
<head>
<meta charset="utf-8">
<title>Tiny Brookvale – Kids Haircuts Flyer</title>
<link rel="stylesheet" href="https://fonts.googleapis.com/css2?family=Oswald:wght@500;700&family=Bebas+Neue&display=swap">
<style>
  :root {
    --white: #ffffff;
    --blue-bright: #1f6fe6;
    --blue-deep: #0b45b8;
    --blue-mid: #3177b5;
    --blue-light: #85acd3;
    --navy: #1a2330;
    --navy-soft: #243040;
    --phone-cyan: #45c3ff;
    --trim-brown: #6b4a2b;
    --photo-skin: #d9b59a;
    --photo-hair: #8a6a4e;
    --photo-light: #eae4de;
  }
  * { margin: 0; padding: 0; box-sizing: border-box; }
  html, body { width: 877px; height: 1200px; overflow: hidden; background: var(--white); }
  .flyer {
    position: relative;
    width: 877px;
    height: 1200px;
    overflow: hidden;
    background: var(--white);
    font-family: "Oswald", "Arial Narrow", sans-serif;
  }
  .flyer > * { position: absolute; }

  .photo-salon-top {
    left: 380px; top: 110px; width: 497px; height: 520px;
    background: radial-gradient(ellipse at 45% 45%, var(--photo-skin) 0%, var(--photo-hair) 35%, var(--photo-light) 70%, var(--white) 100%);
  }
  .backdrop { left: 0; top: 0; width: 877px; height: 1200px; }

  .brand {
    left: 70px; top: 70px;
    display: flex; align-items: center; gap: 14px;
  }
  .brand-dot { width: 54px; height: 54px; border-radius: 50%; background: var(--blue-mid); }
  .brand-name {
    font-family: "Oswald", sans-serif; font-weight: 700;
    font-size: 44px; line-height: 1; color: var(--blue-mid);
  }

  .photo-portrait {
    left: 76px; top: 488px; width: 324px; height: 324px; border-radius: 50%;
    border: 10px solid var(--white);
    background: radial-gradient(circle at 50% 40%, var(--photo-skin) 0%, #b88c6c 40%, #e8ddd0 75%);
  }

  .headline {
    left: 420px; top: 560px; width: 440px;
    color: var(--white); text-align: center;
    font-family: "Bebas Neue", "Oswald", sans-serif;
    text-shadow: 2px 2px 0 var(--navy);
    line-height: 0.95;
  }
  .headline-lead { font-size: 46px; }
  .headline-main { font-size: 108px; line-height: 0.9; }
  .headline-tail { font-size: 46px; }

  .phone {
    left: 470px; top: 820px;
    display: flex; align-items: center; gap: 12px;
    color: var(--phone-cyan);
    font-family: "Bebas Neue", "Oswald", sans-serif; font-size: 58px; line-height: 1;
  }
  .phone-icon { width: 46px; height: 46px; }

  .services {
    left: 0; top: 905px; width: 420px; height: 195px;
    background: var(--blue-deep);
  }
  .mascot-area {
    left: 18px; top: 880px; width: 150px; height: 225px; border-radius: 40px;
    background: linear-gradient(180deg, #e6c79a, #c9d3e4);
  }
  .services-title {
    left: 180px; top: 920px;
    color: var(--white); font-family: "Oswald", sans-serif; font-weight: 700;
    font-size: 44px; font-style: italic;
  }
  .services-list {
    left: 190px; top: 990px; width: 210px; list-style: none; text-align: center;
    color: var(--white); font-family: "Oswald", sans-serif; font-weight: 500;
    font-size: 25px; line-height: 1.3;
  }

  .photo-salon-bottom {
    left: 420px; top: 895px; width: 440px; height: 210px;
    background: linear-gradient(120deg, #5a4a3e 0%, var(--photo-skin) 45%, #c9a880 70%, #3a3a3a 100%);
  }

  .footer {
    left: 0; top: 1120px; width: 877px; height: 80px;
    display: flex; align-items: center; justify-content: space-around;
    color: var(--white); font-family: "Oswald", sans-serif; font-weight: 500; font-size: 24px;
  }
  .contact { display: flex; align-items: center; gap: 10px; text-transform: uppercase; }
  .contact-icon { width: 32px; height: 32px; }
</style>
</head>
<body>
<main class="flyer">
  <div class="photo-salon-top" role="img" aria-label="Photo of a boy having his hair cut with scissors and comb"></div>

  <svg class="backdrop" viewBox="0 0 877 1200" aria-hidden="true">
    <path d="M300,0 L877,0 L877,150 C760,85 560,35 300,0 Z" fill="var(--trim-brown)"/>
    <path d="M330,0 L877,0 L877,135 C760,72 570,28 330,0 Z" fill="var(--blue-bright)"/>
    <path d="M420,0 L877,0 L877,100 C780,50 600,18 420,0 Z" fill="var(--blue-deep)"/>
    <path d="M0,560 C90,440 260,410 470,430 C650,445 790,480 877,470 L877,1200 L0,1200 Z" fill="var(--blue-light)"/>
    <path d="M0,590 C100,470 270,445 470,462 C650,478 790,510 877,505 L877,1200 L0,1200 Z" fill="var(--blue-bright)"/>
    <path d="M0,640 C110,520 280,495 470,512 C640,528 790,555 877,550 L877,1200 L0,1200 Z" fill="var(--blue-deep)"/>
    <path d="M400,650 C540,610 720,600 877,610 L877,1200 L0,1200 L0,870 C150,860 300,760 400,650 Z" fill="var(--navy)"/>
    <rect x="0" y="1105" width="877" height="95" fill="var(--navy-soft)"/>
  </svg>

  <div class="brand">
    <span class="brand-dot"></span>
    <span class="brand-name">Tiny Brookvale</span>
  </div>

  <div class="photo-portrait" role="img" aria-label="Portrait photo of a smiling boy with a fresh haircut"></div>

  <h1 class="headline">
    <span class="headline-lead">Have your child's</span><br>
    <span class="headline-main">Hair cut</span><br>
    <span class="headline-tail">at our new salon</span><br>
    <span class="headline-tail">just for little people!</span>
  </h1>

  <p class="phone">
    <svg class="phone-icon" viewBox="0 0 46 46" aria-hidden="true">
      <circle cx="23" cy="23" r="22" fill="var(--phone-cyan)"/>
      <path d="M15,12 L20,12 L22,18 L19,21 C21,25 23,27 27,29 L30,26 L36,28 L36,33 C36,35 34,36 32,36 C21,35 12,26 11,15 C11,13 13,12 15,12 Z" fill="var(--navy)"/>
    </svg>
    0207 514 0627
  </p>

  <div class="services" aria-hidden="true"></div>
  <div class="mascot-area" role="img" aria-label="Illustration of the shop's waving mascot character"></div>
  <h2 class="services-title">Services:</h2>
  <ul class="services-list">
    <li>KIDS CLOTHES</li>
    <li>BABYWEAR</li>
    <li>TOY SHOP</li>
  </ul>

  <div class="photo-salon-bottom" role="img" aria-label="Photo of a toddler having a haircut in the salon"></div>

  <footer class="footer">
    <span class="contact">
      <svg class="contact-icon" viewBox="0 0 32 32" aria-hidden="true">
        <circle cx="16" cy="16" r="15" fill="var(--white)"/>
        <rect x="8" y="10" width="16" height="12" rx="1" fill="none" stroke="var(--navy)" stroke-width="2"/>
        <path d="M8,11 L16,17 L24,11" fill="none" stroke="var(--navy)" stroke-width="2"/>
      </svg>
      shop@tinybrookvale.com
    </span>
    <span class="contact">
      <svg class="contact-icon" viewBox="0 0 32 32" aria-hidden="true">
        <circle cx="16" cy="16" r="15" fill="var(--white)"/>
      </svg>
      @tinybrookvale
    </span>
  </footer>
</main>
</body>
</html>
```